International Petrochemical business needs a web design for Clearway Desk system

We need a web design for a "Clearway Desk" system for an international petrochemical company. The web site is used internally within the company. It is hosted by an internal department which provides government permit request service for other departments.

We would like to see designs of two pages using color light blue. (home page, internal page as attached).
Home Page:
1. Header has a background image and small animation. Header on home page can be taller than the header of the internal page.
2. Layout as attached.

Internal Page:
1. Header can use the same background image as the home page and can be shorter to utilize the page for content.
2. The blue icon behind every captions represent an icon. When user move mouse over this icon, it displays the caption in Thai language as a tooltip. This icon needs to be redesign.

The final design should communicate the followings:
- Excellent service provided system in terms of time and accurary
- Rapid growth of business via building petrochemical refinery plant

For Internal Page, the blue circle behind every captions represent an icon. When mouse over this icon, a tool tip showing the caption in Thai language is shown. Please also design this icon..

There are more feedbacks from customer as followed:

1. Banner should consists of 
    1.1 "Approved" stamp on paper
    1.2 An image of Garuda. It is used on every government documents in Thailand
    1.3 Image of petrochemical plant
2. Each menu item (Home, Permit, Search, etc) should have different colors. Drop down menu will use the same color as its parent menu item.
3. Overall tone of the web page should be light blue with background of the body the web page in white
4. "New Request" button should use green color with icon on it
5. Table header of each box in the body of the page should use dark blue background with text in white

Please kindly submit your revisions.
Thank you.

Reason: We get some late feedbacks from customers which was just updated to all designers.

• 1. Design for 1024x768 screen resolution
2. Use light blue theme
3. Background of header where the company logo is must have white background

```html
<!DOCTYPE html>
<html lang="en">
<head>
<meta charset="utf-8">
<title>Clearway Desk – Home</title>
<link href="https://fonts.googleapis.com/css2?family=Open+Sans:wght@400;600;700;800&display=swap" rel="stylesheet">
<style>
:root{
  --page-bg:#b6daf0;
  --panel-bg:#f3f9fd;
  --title-blue:#0b3f8a;
  --title-edge:#06306c;
  --head-row:#dbe8f8;
  --head-text:#164b91;
  --row-alt:#f1f6fb;
  --cell-line:#dfe7ef;
  --link:#1c4f9c;
  --text:#3a3f46;
  --active-nav:#1ba3e0;
  --go-green:#5aa81a;
  --go-green-dark:#3f8a0f;
}
*{box-sizing:border-box;margin:0;padding:0}
html,body{width:910px;height:1200px;overflow:hidden}
body{background:var(--page-bg);font-family:"Open Sans",Arial,sans-serif;color:var(--text);position:relative}
.topbar{position:absolute;left:67px;top:0;width:778px;height:59px;background:linear-gradient(#ffffff,#e6ebee);box-shadow:0 1px 3px rgba(0,0,0,.15)}
.brand{position:absolute;left:82px;top:0;width:179px;height:78px;background:#fff;box-shadow:0 1px 4px rgba(0,0,0,.2);display:flex;align-items:center;gap:8px;padding-left:12px;z-index:3}
.brand-dot{width:22px;height:22px;border-radius:50%;background:#1ba3e0;flex:none}
.brand-name{font-weight:700;font-size:12.5px;line-height:14px;color:#1a2f7a}
.main-nav{position:absolute;left:455px;top:0;display:flex;height:59px;z-index:3}
.main-nav a{display:flex;align-items:center;justify-content:center;font-size:11.5px;color:#555;text-decoration:none;border-left:1px solid #e2e6e9;height:59px}
.main-nav a.active{background:var(--active-nav);color:#fff;border-left:none}
.banner{position:absolute;left:67px;top:59px;width:778px;height:166px;background:linear-gradient(180deg,#5fc2ee 0%,#a7dcf3 45%,#6f93b6 72%,#1d2d4a 88%,#b6daf0 100%)}
.badge{position:absolute;top:162px;width:54px;height:54px;border-radius:50%;background:radial-gradient(circle,#ffffff 0%,#dbe9f3 70%,#c3d8e8 100%);box-shadow:0 1px 3px rgba(0,0,0,.25)}
.panel{position:absolute;left:67px;width:778px;background:radial-gradient(ellipse at center,#ffffff 40%,var(--panel-bg) 100%);box-shadow:0 0 4px rgba(0,0,0,.1)}
.box{position:absolute}
.box-title{height:29px;background:var(--title-blue);border:2px solid var(--title-edge);border-radius:7px 7px 0 0;color:#fff;font-size:17px;line-height:25px;padding-left:10px}
table{border-collapse:collapse;width:100%;font-size:11px;table-layout:fixed}
th{height:27px;background:var(--head-row);color:var(--head-text);font-weight:600;text-align:left;padding-left:12px}
td{height:36px;padding-left:12px;border-left:1px solid var(--cell-line)}
td:first-child{border-left:none}
tbody tr{background:#fff}
tbody tr:nth-child(even){background:var(--row-alt)}
td a{color:var(--link)}
.status{color:var(--link)}
.pager{position:absolute;display:flex;align-items:center;gap:0;font-size:8.5px;color:#333}
.pager span{width:19px;text-align:center}
.pager .current{width:14px;height:14px;line-height:14px;background:var(--title-blue);color:#fff;margin:0 2.5px}
.pager svg{display:block}
.go-btn{position:absolute;left:463px;top:829px;width:366px;height:91px;border-radius:5px;background:linear-gradient(#6cbc1f,var(--go-green) 60%,var(--go-green-dark));display:flex;align-items:center;gap:14px;padding-left:16px;color:#fff;font-weight:800;font-size:38px;text-decoration:none;box-shadow:0 1px 2px rgba(0,0,0,.2)}
.plain-table th{background:#fff}
.plain-table td{height:35px}
.plain-table tbody tr{background:#fff}
.footer-nav{position:absolute;left:67px;top:1167px;font-size:9.5px;display:flex;gap:7px}
.footer-nav a{color:#111;text-decoration:none}
.copyright{position:absolute;right:65px;top:1167px;font-size:9.5px;color:#111}
</style>
</head>
<body>

<div class="topbar"></div>
<div class="brand"><span class="brand-dot"></span><span class="brand-name">NORTHBAY<br>PETROCHEMICAL</span></div>
<nav class="main-nav">
  <a class="active" href="#" style="width:58px">Home</a>
  <a href="#" style="width:70px">Permits</a>
  <a href="#" style="width:62px">Search</a>
  <a href="#" style="width:66px">Report</a>
  <a href="#" style="width:62px">Admin</a>
  <a href="#" style="width:56px;border-right:1px solid #e2e6e9">Help</a>
</nav>
<div class="banner" role="img" aria-label="Petrochemical plant with chimneys and cooling tower at dusk by the water"></div>
<div class="badge" style="left:729px" role="img" aria-label="Approved stamp on paper badge"></div>
<div class="badge" style="left:790px" role="img" aria-label="Government emblem badge"></div>

<!-- Requests panel -->
<section class="panel" style="top:226px;height:274px">
  <div class="box" style="left:15px;top:22px;width:365px">
    <div class="box-title">New Request</div>
    <table>
      <colgroup><col style="width:122px"><col style="width:154px"><col></colgroup>
      <thead><tr><th>Request No.</th><th>Requested Date</th><th>Branch</th></tr></thead>
      <tbody>
        <tr><td><a href="#">56-0003</a></td><td>20-4-2013</td><td>GC 1</td></tr>
        <tr><td><a href="#">56-0004</a></td><td>21-4-2013</td><td>GC 2</td></tr>
        <tr><td><a href="#">56-0005</a></td><td>22-4-2013</td><td>GC 3</td></tr>
        <tr><td><a href="#">56-0006</a></td><td>23-4-2013</td><td>GC 4</td></tr>
      </tbody>
    </table>
  </div>
  <div class="box" style="left:396px;top:22px;width:365px">
    <div class="box-title">My Working Request</div>
    <table>
      <colgroup><col style="width:122px"><col style="width:114px"><col></colgroup>
      <thead><tr><th>Request No.</th><th>Requested Date</th><th>Status</th></tr></thead>
      <tbody>
        <tr><td><a href="#">22-0200</a></td><td>25-3-2013</td><td class="status">Waiting for process</td></tr>
        <tr><td><a href="#">22-0210</a></td><td>24-3-2013</td><td class="status">in progress</td></tr>
        <tr><td><a href="#">55-0300</a></td><td>18-1-2013</td><td class="status">Incomplete document</td></tr>
        <tr><td><a href="#">55-0301</a></td><td>20-1-2013</td><td class="status">Cancel Requested</td></tr>
      </tbody>
    </table>
  </div>
  <div class="pager" style="left:15px;top:232px"><svg width="14" height="10"><path d="M1 5 L6 1 V3.5 H13 V6.5 H6 V9 Z" fill="#3a9ad9"/></svg><span>1</span><span class="current">2</span><span>3</span><span>4</span><span>5</span><svg width="14" height="10"><path d="M13 5 L8 1 V3.5 H1 V6.5 H8 V9 Z" fill="#3a9ad9"/></svg></div>
  <div class="pager" style="left:396px;top:232px"><svg width="14" height="10"><path d="M1 5 L6 1 V3.5 H13 V6.5 H6 V9 Z" fill="#3a9ad9"/></svg><span>1</span><span class="current">2</span><span>3</span><span>4</span><span>5</span><svg width="14" height="10"><path d="M13 5 L8 1 V3.5 H1 V6.5 H8 V9 Z" fill="#3a9ad9"/></svg></div>
</section>

<!-- Expiring permits panel -->
<section class="panel" style="top:515px;height:275px">
  <div class="box" style="left:15px;top:23px;width:746px">
    <div class="box-title">Expiring Permits</div>
    <table>
      <thead><tr><th>Permit No.</th><th>Expire Date</th><th>Permit Name</th><th>Branch</th><th>Required Time (Day)</th><th>Due Date</th></tr></thead>
      <tbody>
        <tr><td><a href="#">AB56007</a></td><td>20-4-2013</td><td><a href="#">Permit Name #10</a></td><td class="status">GC 1</td><td class="status">30</td><td class="status">-40</td></tr>
        <tr><td><a href="#">BIO5502</a></td><td>21-4-2013</td><td><a href="#">Permit Name #20</a></td><td class="status">GC 2</td><td class="status">60</td><td class="status">15</td></tr>
        <tr><td><a href="#">TS34821</a></td><td>22-4-2013</td><td><a href="#">Permit Name #30</a></td><td class="status">GC 3</td><td class="status">90</td><td class="status">25</td></tr>
        <tr><td><a href="#">GD47515</a></td><td>23-4-2013</td><td><a href="#">Permit Name #40</a></td><td class="status">GC 4</td><td class="status">120</td><td class="status">-90</td></tr>
      </tbody>
    </table>
  </div>
  <div class="pager" style="left:15px;top:233px"><svg width="14" height="10"><path d="M1 5 L6 1 V3.5 H13 V6.5 H6 V9 Z" fill="#3a9ad9"/></svg><span>1</span><span class="current">2</span><span>3</span><span>4</span><span>5</span><svg width="14" height="10"><path d="M13 5 L8 1 V3.5 H1 V6.5 H8 V9 Z" fill="#3a9ad9"/></svg></div>
</section>

<!-- Progress panel -->
<section class="panel" style="top:806px;height:340px">
  <div class="box" style="left:15px;top:23px;width:365px">
    <div class="box-title">My in Progress Requests</div>
    <table>
      <colgroup><col style="width:122px"><col style="width:114px"><col></colgroup>
      <thead><tr><th>Request No.</th><th>Requested Date</th><th>Status</th></tr></thead>
      <tbody>
        <tr><td><a href="#">56-0003</a></td><td>20-4-2013</td><td class="status">Waiting for process</td></tr>
        <tr><td><a href="#">56-0004</a></td><td>21-4-2013</td><td class="status">in progress</td></tr>
        <tr><td><a href="#">56-0005</a></td><td>22-4-2013</td><td class="status">Incomplete document</td></tr>
        <tr><td><a href="#">56-0006</a></td><td>23-4-2013</td><td class="status">Cancel Requested</td></tr>
        <tr><td><a href="#">56-0007</a></td><td>24-4-2013</td><td class="status">In progress</td></tr>
        <tr><td><a href="#">56-0008</a></td><td>25-4-2013</td><td class="status">Cancel Requested</td></tr>
      </tbody>
    </table>
  </div>
  <div class="box" style="left:396px;top:130px;width:365px">
    <div class="box-title">Recent Completed Requests</div>
    <table class="plain-table">
      <colgroup><col style="width:182px"><col></colgroup>
      <thead><tr><th style="height:24px">Request No.</th><th>Completed Date</th></tr></thead>
      <tbody>
        <tr><td><a href="#">22-0200</a></td><td>25-3-2013</td></tr>
        <tr><td><a href="#">22-0210</a></td><td>24-3-2013</td></tr>
        <tr><td><a href="#">55-0300</a></td><td>18-1-2013</td></tr>
      </tbody>
    </table>
  </div>
  <div class="pager" style="left:15px;top:308px"><svg width="14" height="10"><path d="M1 5 L6 1 V3.5 H13 V6.5 H6 V9 Z" fill="#3a9ad9"/></svg><span>1</span><span class="current">2</span><span>3</span><span>4</span><span>5</span><svg width="14" height="10"><path d="M13 5 L8 1 V3.5 H1 V6.5 H8 V9 Z" fill="#3a9ad9"/></svg></div>
  <div class="pager" style="left:396px;top:308px"><svg width="14" height="10"><path d="M1 5 L6 1 V3.5 H13 V6.5 H6 V9 Z" fill="#3a9ad9"/></svg><span>1</span><span class="current">2</span><span>3</span><span>4</span><span>5</span><svg width="14" height="10"><path d="M13 5 L8 1 V3.5 H1 V6.5 H8 V9 Z" fill="#3a9ad9"/></svg></div>
</section>

<a class="go-btn" href="#">
  <svg width="62" height="56" viewBox="0 0 62 56" aria-hidden="true">
    <rect x="4" y="24" width="44" height="28" rx="3" fill="none" stroke="#fff" stroke-width="4"/>
    <line x1="11" y1="34" x2="26" y2="34" stroke="#fff" stroke-width="3"/>
    <line x1="11" y1="42" x2="22" y2="42" stroke="#fff" stroke-width="3"/>
    <path d="M28 40 L50 6 L58 11 L36 45 L26 48 Z" fill="#fff"/>
    <path d="M50 6 L58 11" stroke="#5aa81a" stroke-width="2"/>
  </svg>
  NEW REQUEST
</a>

<nav class="footer-nav"><a href="#">Home</a><a href="#">Permits</a><a href="#">Search</a><a href="#">Report</a><a href="#">Admin</a><a href="#">Help</a></nav>
<div class="copyright">© Copyrights 2013 All rights Reserved</div>

</body>
</html>
```